We need a web page design for a new company called "Quarry". We provide an innovative music sharing mobile application that allows music listeners to share their music without paying for a monthly subscription. We would like to incorporate the attached logo and color scheme. The final design should communicate music gifting and sharing.

Industry/Entity Type

It Company

```html
<!DOCTYPE html>
<html lang="en">
<head>
<meta charset="utf-8">
<title>Quarry – Share Your Music</title>
<link href="https://fonts.googleapis.com/css2?family=Lato:wght@400;700&family=Oswald:wght@400&family=Courgette&family=Roboto:wght@400;700&display=swap" rel="stylesheet">
<style>
:root{
  --green:#5ba40a;
  --green-dark:#4a8a06;
  --ink:#222;
  --text:#444;
  --muted:#666;
  --panel:#ececec;
  --footer:#333;
  --white:#fff;
  --black:#111;
}
*{box-sizing:border-box;margin:0;padding:0}
html,body{width:714px;height:1200px;overflow:hidden}
body{position:relative;font-family:"Lato",Arial,sans-serif;background:var(--white);color:var(--text)}
.abs{position:absolute}

/* header */
.site-header{left:0;top:0;width:714px;height:58px;background:var(--green)}
.brand{left:80px;top:10px;display:flex;align-items:center;gap:8px;color:var(--white);font:700 30px/1 "Lato",sans-serif}
.brand-dot{width:30px;height:30px;border-radius:50%;background:var(--white)}
.search{left:269px;top:23px;width:140px;height:16px;display:flex}
.search-input{flex:1;background:var(--white);border:0;font:8px "Roboto",sans-serif;color:#555;padding:3px 4px}
.search-btn{width:16px;height:16px;background:var(--black);display:flex;align-items:center;justify-content:center}
.main-nav{left:445px;top:19px;display:flex;align-items:center;gap:0;font:400 13px "Roboto",sans-serif;color:var(--white)}
.main-nav a{color:var(--white);text-decoration:none;margin-right:11px}
.main-nav .upload{background:var(--ink);padding:3px 7px;margin-right:0;font-weight:700}

/* hero */
.hero{left:0;top:58px;width:714px;height:260px;background:radial-gradient(ellipse at 390px 120px,#f3c27a 0%,#c86a2a 22%,#8a3a14 50%,#4a1c0a 100%)}
.hero-title{left:80px;top:142px;width:215px;text-align:center;font:22px/33px "Courgette",cursive;color:var(--white)}
.hero-dots{left:137px;top:297px;display:flex;gap:6px}
.hero-dots span{width:11px;height:11px;border-radius:50%;background:var(--white)}
.hero-dots span.active{background:var(--green)}

/* features */
.features{left:0;top:318px;width:714px;height:210px;background:var(--panel);border-top:2px solid var(--green)}
.feature{top:24px;width:144px;text-align:center}
.feature-icon{width:82px;height:82px;margin:0 auto;border-radius:50%;background:var(--green);border:3px solid var(--white);box-shadow:0 0 0 2px var(--ink);display:flex;align-items:center;justify-content:center}
.feature h3{margin-top:18px;font:700 10.5px "Roboto",sans-serif;color:var(--ink)}
.feature p{margin-top:9px;font:8px/10.5px "Roboto",sans-serif;color:var(--text)}

/* call to action */
.cta{left:0;top:528px;width:714px;height:54px;background:var(--green)}
.cta-text{left:80px;top:534px;font:400 17px/21px "Oswald",sans-serif;color:var(--white)}
.cta-btn{left:502px;top:537px;width:134px;height:36px;border-radius:7px;background:var(--black);border:2px solid #555;color:var(--white);font:400 18px/32px "Oswald",sans-serif;text-align:center}

/* trending */
.section-title{left:0;top:597px;width:714px;text-align:center;font:700 17px "Lato",sans-serif;color:var(--green)}
.category{left:78px;top:640px;width:139px;height:186px;background:var(--green)}
.category-head{height:27px;background:var(--black);color:var(--white);font:700 14px/27px "Lato",sans-serif;padding-left:10px}
.cat-row{display:flex;justify-content:space-between;align-items:center;height:16.5px;padding:0 4px 0 10px;border-bottom:1px solid #7cc23a;font:700 7.5px "Roboto",sans-serif;color:var(--white)}
.cat-row.sub{background:var(--green-dark)}
.cat-row i{width:10px;height:10px;border-radius:50%;background:var(--white);display:block}
.poster{left:78px;top:841px;width:139px;height:185px;background:linear-gradient(160deg,#3a2a22,#1a1410 60%,#0d0a08)}
.card{width:123px;height:186px;border:1px solid #999;background:var(--white);padding:2px}
.card-media{height:101px}
.card h4{margin:6px 0 0 3px;font:700 9.5px/12px "Lato",sans-serif;color:var(--green)}
.card p{margin:5px 0 0 3px;font:7.5px/10.5px "Roboto",sans-serif;color:var(--text)}
.card-actions{position:absolute;left:5px;bottom:6px;display:flex;gap:4px}
.card-actions span{font:700 7.5px/11px "Roboto",sans-serif;color:var(--white);text-align:center}
.gift{width:34px;background:#666}
.share{width:45px;background:var(--green)}
.m-dusk{background:linear-gradient(180deg,#c9bfa9,#514a3e 55%,#1a1a1a)}
.m-club{background:linear-gradient(135deg,#6a2a8a,#1a1030 50%,#d03aa0)}
.m-stage{background:linear-gradient(135deg,#1a3a5a,#7aa8c8 50%,#0e1a28)}

/* footer */
.site-footer{left:0;top:1049px;width:714px;height:127px;background:var(--footer);color:var(--white)}
.foot-col{top:1062px}
.foot-col h5{font:400 13px "Lato",sans-serif;padding-bottom:3px;border-bottom:1px solid #555;width:90px}
.foot-links{list-style:none;margin-top:6px;font:7.5px/15px "Roboto",sans-serif}
.foot-links li::before{content:"› "}
.newsletter p{margin-top:7px;font:7.5px/10.5px "Roboto",sans-serif;width:125px}
.email{margin-top:5px;width:127px;height:15px;background:#666;font:7px/15px "Roboto",sans-serif;padding-left:4px}
.subscribe{margin-top:7px;width:53px;height:16px;background:var(--green);font:700 7.5px/16px "Roboto",sans-serif;text-align:center}
.social{list-style:none;margin-top:8px;font:7.5px "Roboto",sans-serif}
.social li{display:flex;align-items:center;gap:6px;height:21.5px}
.social i{width:13px;height:13px;display:block;background:#4a6ea8}
.foot-mark{left:560px;top:1088px;display:flex;flex-direction:column;align-items:center;gap:6px;font:700 13px "Lato",sans-serif;color:var(--white)}
.foot-mark span{width:58px;height:58px;border-radius:50%;background:var(--white)}
.bottom-bar{left:0;top:1176px;width:714px;height:24px;background:var(--green);color:var(--white);font:7.5px/24px "Roboto",sans-serif;text-align:center}
</style>
</head>
<body>

<header class="site-header abs"></header>
<div class="brand abs"><span class="brand-dot"></span>Quarry</div>
<div class="search abs"><span class="search-input">Search</span><span class="search-btn"><svg width="9" height="9" viewBox="0 0 10 10"><circle cx="4" cy="4" r="3" fill="none" stroke="#fff" stroke-width="1.5"/><line x1="6.2" y1="6.2" x2="9" y2="9" stroke="#fff" stroke-width="1.5"/></svg></span></div>
<nav class="main-nav abs"><a>People</a><a>Sign Up</a><a>Login</a><a class="upload">Upload</a></nav>

<section class="hero abs" role="img" aria-label="Singer with eyes closed surrounded by floating feathers and music notes in warm amber light"></section>
<h1 class="hero-title abs">Lorem ipsum dolor sit amet consectetuer adipiscing elit</h1>
<div class="hero-dots abs"><span class="active"></span><span></span><span></span><span></span></div>

<section class="features abs">
  <div class="feature abs" style="left:73px">
    <div class="feature-icon"><svg width="44" height="40" viewBox="0 0 44 40"><path d="M22 2 L34 14 H26 V24 H18 V14 H10Z" fill="#111"/><rect x="4" y="27" width="36" height="11" rx="2" fill="#111"/><circle cx="30" cy="32.5" r="1.5" fill="#5ba40a"/><circle cx="35" cy="32.5" r="1.5" fill="#5ba40a"/></svg></div>
    <h3>UPLOAD MUSIC &amp; AUDIO</h3>
    <p>Lorem ipsum dolor sit amet consectetuer adipiscing elit sed diam nonummy nibh euismod tincidunt ut laoreet</p>
  </div>
  <div class="feature abs" style="left:217px">
    <div class="feature-icon"><svg width="44" height="40" viewBox="0 0 44 40"><path d="M4 14 H12 L22 5 V35 L12 26 H4Z" fill="#111"/><path d="M27 14 Q31 20 27 26 M31 10 Q37 20 31 30 M35 6 Q43 20 35 34" fill="none" stroke="#111" stroke-width="3" stroke-linecap="round"/></svg></div>
    <h3>LISTEN &amp; DISCOVER</h3>
    <p>Lorem ipsum dolor sit amet consectetuer adipiscing elit sed diam nonummy nibh euismod tincidunt ut laoreet</p>
  </div>
  <div class="feature abs" style="left:361px">
    <div class="feature-icon"><svg width="44" height="40" viewBox="0 0 44 40"><circle cx="27" cy="12" r="8" fill="#111"/><path d="M13 36 Q15 21 27 21 Q39 21 41 36Z" fill="#111"/><circle cx="16" cy="14" r="7.5" fill="#111" stroke="#5ba40a" stroke-width="2"/><path d="M2 37 Q4 23 16 23 Q28 23 30 37Z" fill="#111" stroke="#5ba40a" stroke-width="2"/></svg></div>
    <h3>CONNECT</h3>
    <p>Lorem ipsum dolor sit amet consectetuer adipiscing elit sed diam nonummy nibh euismod tincidunt ut laoreet</p>
  </div>
  <div class="feature abs" style="left:505px">
    <div class="feature-icon"><svg width="44" height="44" viewBox="0 0 44 44"><line x1="31" y1="10" x2="13" y2="22" stroke="#111" stroke-width="3"/><line x1="13" y1="22" x2="31" y2="34" stroke="#111" stroke-width="3"/><circle cx="31" cy="10" r="7" fill="#111"/><circle cx="13" cy="22" r="7" fill="#111"/><circle cx="31" cy="34" r="7" fill="#111"/></svg></div>
    <h3>SHARE</h3>
    <p>Lorem ipsum dolor sit amet consectetuer adipiscing elit sed diam nonummy nibh euismod tincidunt ut laoreet</p>
  </div>
</section>

<section class="cta abs"></section>
<p class="cta-text abs">So are you ready to discover new music and sounds and<br>share them with the world?</p>
<div class="cta-btn abs">SIGN UP NOW!</div>

<h2 class="section-title abs">Trending Music &amp; Audio</h2>

<aside class="category abs">
  <div class="category-head">Category</div>
  <div class="cat-row">Lorem ipsum dolor sit<i></i></div>
  <div class="cat-row sub">&gt; Lorem ipsum dolor sit</div>
  <div class="cat-row sub">&gt; Lorem ipsum dolor sit</div>
  <div class="cat-row sub">&gt; Lorem ipsum dolor sit</div>
  <div class="cat-row sub">&gt; Lorem ipsum dolor sit</div>
  <div class="cat-row sub">&gt; Lorem ipsum dolor sit</div>
  <div class="cat-row">Lorem ipsum dolor sit<i></i></div>
  <div class="cat-row">Lorem ipsum dolor sit<i></i></div>
  <div class="cat-row">Lorem ipsum dolor sit<i></i></div>
</aside>
<div class="poster abs" role="img" aria-label="Event poster for a writing club night with a glass of beer, a quill and a radio"></div>

<article class="card abs" style="left:235px;top:640px"><div class="card-media m-dusk" role="img" aria-label="Audio book cover: dark city skyline against a hazy sunset"></div><h4>Northern Front Audio Book</h4><p>Lorem ipsum dolor sit amet consectetuer adipiscing</p><div class="card-actions"><span class="gift">Gift</span><span class="share">Share</span></div></article>
<article class="card abs" style="left:375px;top:640px"><div class="card-media m-club" role="img" aria-label="DJ at the decks under purple club lights"></div><h4>Ray Solis Tribute To Marco Lune…</h4><p>Lorem ipsum dolor sit amet consectetuer adipiscing</p><div class="card-actions"><span class="gift">Gift</span><span class="share">Share</span></div></article>
<article class="card abs" style="left:514px;top:640px"><div class="card-media m-stage" role="img" aria-label="DJ performing on stage in front of a blue lit screen"></div><h4>Deep Room Halifax</h4><p>Lorem ipsum dolor sit amet consectetuer adipiscing</p><div class="card-actions"><span class="gift">Gift</span><span class="share">Share</span></div></article>

<article class="card abs" style="left:235px;top:841px"><div class="card-media m-dusk" role="img" aria-label="Audio book cover: dark city skyline against a hazy sunset"></div><h4>Northern Front Audio Book</h4><p>Lorem ipsum dolor sit amet consectetuer adipiscing</p><div class="card-actions"><span class="gift">Gift</span><span class="share">Share</span></div></article>
<article class="card abs" style="left:375px;top:841px"><div class="card-media m-club" role="img" aria-label="DJ at the decks under purple club lights"></div><h4>Ray Solis Tribute To Marco Lune…</h4><p>Lorem ipsum dolor sit amet consectetuer adipiscing</p><div class="card-actions"><span class="gift">Gift</span><span class="share">Share</span></div></article>
<article class="card abs" style="left:514px;top:841px"><div class="card-media m-stage" role="img" aria-label="DJ performing on stage in front of a blue lit screen"></div><h4>Deep Room Halifax</h4><p>Lorem ipsum dolor sit amet consectetuer adipiscing</p><div class="card-actions"><span class="gift">Gift</span><span class="share">Share</span></div></article>

<footer class="site-footer abs"></footer>
<div class="foot-col abs" style="left:78px;color:#fff">
  <h5>Quick Links</h5>
  <ul class="foot-links"><li>About Us</li><li>People</li><li>Sign Up</li><li>Login</li><li>Upload</li></ul>
</div>
<div class="foot-col newsletter abs" style="left:230px;color:#fff">
  <h5 style="width:127px">Newsletter</h5>
  <p>Signup with us and get update in your inbox.</p>
  <div class="email">Email address</div>
  <div class="subscribe">SUBSCRIBE</div>
</div>
<div class="foot-col abs" style="left:423px;color:#fff">
  <h5 style="width:75px">Follow Us On</h5>
  <ul class="social">
    <li><i></i>Circlebook</li>
    <li><i style="background:#3aa6e0"></i>Chirper</li>
    <li><i style="background:#c8322a"></i>Tubecast</li>
    <li><i style="background:#1a6aa8"></i>Linkwork</li>
  </ul>
</div>
<div class="foot-mark abs"><span></span>Quarry</div>
<div class="bottom-bar abs">© 2014 QuarryMusic. All Rights Reserved.</div>

</body>
</html>
```